web design needed for jewellery inspired temporary tattoo company

Hi There

I need a web design for a new company I'm launching called coral glow luxe
Im a retailer of flash tattoos - temporary gold and silver metallic tattoos

These are the next new craze with many celebrities already displaying them whilst being lapped on their holidays

i need a very classy upmarket wow web design with an e commerce shop attached

I also offer marlow q bronze mist so will need a page to link to where people can get a tan and tattoo - so maybe as a box on the main page

As A guide I'm looking for someone to put their unique spin on an american website which is currently selling the same type of product
www.glintmarkz.com

the final design should oozzzz 'rich list ' coral luxe - think st tropez Monaco and needs to be linked to all my social media

please seepintrest flash tattoos for what we sell
I've attached my logo

I can't wait to hear from you all
many Thanks

Fiona Dembrey
www.coralglowluxe.co.uk

Target Market(s)

20 to 30's young party rich list glamous girls - festival boho cool beach LA

Industry/Entity Type

It Company

Number of Pages Required

3 page

Font styles to use
Script

Requirements
Must have
• a beach feel
• pictures of people wearing the tattoos
• an ecommerce site
• be easy to navigate
• my logo
• the wow factor
Nice to have
• a really classy expensive feel to the website
Should not have
• a cheap plain look

```html
<!DOCTYPE html>
<html lang="en">
<head>
<meta charset="utf-8">
<title>Coral Glow Luxe London</title>
<link rel="stylesheet" href="https://fonts.googleapis.com/css2?family=Montserrat:wght@400;500;600;700&family=Great+Vibes&family=Arimo:wght@400&display=swap">
<style>
:root{
  --bar:#0d0d0d;
  --header:#1d1d1d;
  --section:#0f0f0f;
  --footer:#121111;
  --gold:#c9a950;
  --gold-light:#e3c97a;
  --btn-yellow:#f4c520;
  --btn-cream:#f6dc8e;
  --band:#efdc9c;
  --white:#ffffff;
  --muted:#bdbdbd;
  --text-dim:#9a9a9a;
}
*{margin:0;padding:0;box-sizing:border-box}
html,body{width:1200px;height:2169px;overflow:hidden;background:var(--white)}
body{position:relative;font-family:'Montserrat',sans-serif;color:var(--white)}
.abs{position:absolute}
a{color:inherit;text-decoration:none}

/* utility bar */
.utility-bar{left:0;top:0;width:1200px;height:43px;background:var(--bar)}
.search{left:124px;top:9px;width:220px;height:24px;border:1px solid #8a7430;font-size:11px;color:#777;padding:5px 10px}
.search svg{position:absolute;right:6px;top:4px}
.utility-links{right:85px;top:14px;display:flex;gap:20px;font-size:10px;letter-spacing:.3px;color:#e6e6e6}

/* header */
.site-header{left:0;top:43px;width:1200px;height:178px;background:var(--header)}
.nav-item{font-size:16px;font-weight:500;letter-spacing:1.5px;color:var(--white);white-space:nowrap}
.nav-home{left:127px;top:100px;width:88px;height:37px;border:1px solid var(--gold);color:var(--gold-light);display:flex;align-items:center;justify-content:center}
.logo{left:486px;top:25px;width:200px;text-align:center;color:var(--gold)}
.logo-mark{width:70px;height:70px;margin:0 auto;border-radius:50%;background:var(--gold)}
.logo-name{margin-top:50px;font-size:21px;font-weight:500;letter-spacing:.5px;white-space:nowrap}
.logo-city{margin-top:4px;font-size:12px;letter-spacing:2px}

/* hero */
.hero{left:0;top:221px;width:1200px;height:551px;background:linear-gradient(120deg,#5b6a3a 0%,#6b4a34 30%,#3e66a8 50%,#5a3b2b 70%,#7b6a4c 100%)}
.hero-title{left:0;top:415px;width:1200px;text-align:center;font-family:'Great Vibes',cursive;font-size:78px;color:var(--white);text-shadow:2px 3px 6px rgba(0,0,0,.6);white-space:nowrap}
.hero-cta{left:536px;top:510px;width:157px;height:37px;background:var(--btn-yellow);color:#1b1b1b;font-size:16px;font-weight:600;letter-spacing:1.5px;display:flex;align-items:center;justify-content:center}
.hero-arrow{top:432px;width:72px;height:72px;border-radius:50%;background:var(--white);display:flex;align-items:center}
.hero-arrow.prev{left:-38px;justify-content:flex-end;padding-right:12px}
.hero-arrow.next{left:1167px;justify-content:flex-start;padding-left:12px}

/* popular */
.popular{left:0;top:772px;width:1200px;height:621px;background:var(--section)}
.section-title{left:0;top:828px;width:1200px;text-align:center;font-size:23px;letter-spacing:2.5px;color:var(--gold)}
.product{top:899px;width:230px}
.product-photo{width:192px;height:175px;border:1px solid #8e8e8e;position:relative;margin-left:6px}
.product-badge{position:absolute;left:0;top:0;width:100%;height:30px;background:rgba(0,0,0,.55);font-size:17px;letter-spacing:3px;text-align:center;line-height:30px;color:#eee}
.product-name{margin-top:19px;font-family:'Arimo',sans-serif;font-size:19px;color:var(--white);white-space:nowrap}
.product-desc{margin-top:8px;font-size:11px;line-height:17px;color:var(--muted);width:200px}
.product-price{margin-top:14px;font-size:14px;color:var(--white)}
.add-to-cart{margin-top:15px;width:107px;height:29px;background:var(--btn-cream);color:#111;font-size:13px;font-weight:700;letter-spacing:.8px;display:flex;align-items:center;justify-content:center}
.view-all{left:487px;top:1290px;width:219px;height:36px;border:1px solid #5a5a5a;color:#e5e5e5;font-size:15px;font-weight:500;letter-spacing:2px;display:flex;align-items:center;justify-content:center}

/* promos */
.promo{border:1px solid #999}
.promo-caption{position:absolute;left:0;top:126px;width:100%;height:38px;background:rgba(20,20,20,.8);font-family:'Great Vibes',cursive;font-size:27px;text-align:center;line-height:38px;color:var(--white)}
.promo-sub{position:absolute;left:0;top:170px;width:100%;text-align:center;font-size:15px;font-weight:600;color:#111;white-space:nowrap}

/* newsletter */
.newsletter{left:0;top:1743px;width:1200px;height:52px;background:var(--band)}
.newsletter-title{left:127px;top:1748px;font-family:'Great Vibes',cursive;font-size:32px;color:#111;white-space:nowrap}
.field{top:1754px;width:217px;height:29px;background:var(--white);border:1px solid #c8c8c8;font-family:'Arimo',sans-serif;font-size:11px;color:#333;padding:7px 12px}
.join{left:937px;top:1754px;width:97px;height:29px;background:#0d0d0d;font-size:13px;font-weight:700;display:flex;align-items:center;justify-content:center}

/* footer */
.site-footer{left:0;top:1795px;width:1200px;height:295px;background:var(--footer)}
.footer-col{top:1848px}
.footer-col h4{font-size:11px;font-weight:600;letter-spacing:.3px;color:#e8e8e8;margin-bottom:21px;white-space:nowrap}
.footer-col li{list-style:none;font-size:11px;line-height:18px;color:var(--text-dim);white-space:nowrap}
.copyright{left:0;top:2037px;width:1200px;text-align:center;font-size:11.5px;color:var(--text-dim)}

/* trust badges */
.trust{left:0;top:2090px;width:1200px;height:79px;background:var(--white)}
.badge{top:2110px;height:38px;border-radius:6px}
</style>
</head>
<body>

<div class="abs utility-bar"></div>
<div class="abs search">Search for Products
  <svg width="14" height="14" viewBox="0 0 14 14"><circle cx="6" cy="6" r="4.5" fill="none" stroke="#c9a950" stroke-width="1.6"/><line x1="9.3" y1="9.3" x2="13" y2="13" stroke="#c9a950" stroke-width="1.8"/></svg>
</div>
<nav class="abs utility-links">
  <a>HOME</a><a>GIFT CERTIFICATES</a><a>SIGN IN OR CREATE AN ACCOUNT</a><a>VIEW CART</a>
</nav>

<header class="abs site-header"></header>
<a class="abs nav-item nav-home">HOME</a>
<a class="abs nav-item" style="left:257px;top:108px">PRODUCTS</a>
<a class="abs nav-item" style="left:408px;top:108px">ABOUT</a>
<a class="abs nav-item" style="left:727px;top:103px">STORE LOCATOR</a>
<a class="abs nav-item" style="left:917px;top:103px">CONTACT US</a>
<div class="abs logo">
  <div class="logo-mark"></div>
  <div class="logo-name">Coral Glow Luxe</div>
  <div class="logo-city">LONDON</div>
</div>

<section class="abs hero" role="img" aria-label="Photo of a woman in a blue top crossing her arms, wearing gold and silver metallic temporary tattoos"></section>
<h1 class="abs hero-title" style="font-weight:400">Some Silver &amp; Gold</h1>
<a class="abs hero-cta">SHOP NOW</a>
<div class="abs hero-arrow prev"><svg width="12" height="18" viewBox="0 0 12 18"><polyline points="9,2 3,9 9,16" fill="none" stroke="#333" stroke-width="2"/></svg></div>
<div class="abs hero-arrow next"><svg width="12" height="18" viewBox="0 0 12 18"><polyline points="3,2 9,9 3,16" fill="none" stroke="#333" stroke-width="2"/></svg></div>

<section class="abs popular"></section>
<h2 class="abs section-title" style="font-weight:400">MOST POPULAR THIS WEEK</h2>

<article class="abs product" style="left:133px">
  <div class="product-photo" role="img" aria-label="Hand and arm wearing lace-style gold tattoos on grass" style="background:linear-gradient(135deg,#3d4a2a,#b08a5c 55%,#6b5236)"><div class="product-badge">NEW ARRIVAL</div></div>
  <div class="product-name">Lorem ipsum dolor sit</div>
  <div class="product-desc">Lorem ipsum dolor sit amet consec-tetur adipisicing elit</div>
  <div class="product-price">$ 6,500</div>
  <a class="add-to-cart">ADD TO CART</a>
</article>
<article class="abs product" style="left:376px">
  <div class="product-photo" role="img" aria-label="Back of a woman at the beach with a gold spine tattoo" style="background:linear-gradient(180deg,#b9c3c8,#8a6a52 55%,#c7b39a)"></div>
  <div class="product-name">Lorem ipsum dolor sit</div>
  <div class="product-desc">Lorem ipsum dolor sit amet consec-tetur adipisicing elit</div>
  <div class="product-price">$ 6,500</div>
  <a class="add-to-cart">ADD TO CART</a>
</article>
<article class="abs product" style="left:620px">
  <div class="product-photo" role="img" aria-label="Wrist wearing a silver flower bracelet tattoo" style="background:linear-gradient(90deg,#2b2520,#c8a98a 50%,#e8e2d6)"></div>
  <div class="product-name">Lorem ipsum dolor sit</div>
  <div class="product-desc">Lorem ipsum dolor sit amet consec-tetur adipisicing elit</div>
  <div class="product-price">$ 6,500</div>
  <a class="add-to-cart">ADD TO CART</a>
</article>
<article class="abs product" style="left:863px">
  <div class="product-photo" role="img" aria-label="Shoulder with a geometric gold tattoo in warm sunset light" style="background:linear-gradient(135deg,#e2a07a,#b0577a 50%,#8a3f6a)"></div>
  <div class="product-name">Lorem ipsum dolor sit</div>
  <div class="product-desc">Lorem ipsum dolor sit amet consec-tetur adipisicing elit</div>
  <div class="product-price">$ 6,500</div>
  <a class="add-to-cart">ADD TO CART</a>
</article>

<a class="abs view-all">VIEW AL PRODUCTS</a>

<div class="abs promo" style="left:126px;top:1436px;width:266px;height:270px;background:linear-gradient(180deg,#2f9aa0 0%,#d7b38c 45%,#b98a64 100%)" role="img" aria-label="Woman seen from behind on the beach with a metallic back tattoo">
  <div class="promo-caption">Wanna Be Friends?</div>
  <div class="promo-sub">FOLLOW US ON FRIENDSPACE</div>
</div>
<div class="abs promo" style="left:409px;top:1436px;width:265px;height:270px;background:linear-gradient(180deg,#c9d3d8 0%,#7a5a45 40%,#a88f86 75%,#5fa6a8 100%)" role="img" aria-label="Woman in a patterned bikini wearing gold body chain tattoos">
  <div class="promo-caption">Celebrities</div>
</div>
<div class="abs promo" style="left:691px;top:1433px;width:378px;height:267px;background:radial-gradient(ellipse at 50% 70%,#e9c9d8 0%,#b0408a 45%,#6a1a52 100%)" role="img" aria-label="Advert for the Marlow Q Bronze Mist tanning range with a row of bottles"></div>

<section class="abs newsletter"></section>
<div class="abs newsletter-title">Sign up for our newsletter</div>
<div class="abs field" style="left:480px">Enter Your Name:</div>
<div class="abs field" style="left:711px">Enter Your Email:</div>
<a class="abs join">JOIN NOW</a>

<footer class="abs site-footer"></footer>
<div class="abs footer-col" style="left:124px"><h4>ABOUT CORAL GLOW LUXE</h4><ul><li>About Us</li><li>Press</li><li>Why Shop With Us</li><li>Affliate Program</li><li>Referral Program</li></ul></div>
<div class="abs footer-col" style="left:301px"><h4>TOP CATEGORIES</h4><ul><li>Earrings</li><li>Bracelets</li><li>Brooches</li><li>Necklaces</li><li>Pendants</li><li>Rings</li><li>Hair accessories</li></ul></div>
<div class="abs footer-col" style="left:495px"><h4>CUSTOMER SERVICES</h4><ul><li>Contact Us</li><li>Live Chat</li><li>FAQs</li><li>Advice Center</li><li>Order Status</li><li>Easy Reorder</li><li>Email Preferences</li></ul></div>
<div class="abs footer-col" style="left:704px"><h4>SHIPPING, RETURN &amp; POLICIES</h4><ul><li>Shipping Policy</li><li>Return Policy</li><li>ReStocker Terms &amp; Conditions</li><li>Policies &amp; Procedures</li></ul></div>
<div class="abs footer-col" style="left:951px"><h4>FIND MORE</h4><ul><li>Site Map</li><li>Links</li><li>My Cart</li><li>My Account</li><li>Shopping List</li><li>Blog</li></ul></div>
<div class="abs copyright">Copyright © 2015 Coralglowluxe.com - All Rights Reserved</div>

<div class="abs trust"></div>
<div class="abs badge" style="left:409px;width:75px;background:#c8282e"></div>
<div class="abs badge" style="left:506px;width:48px;border-radius:50%;background:#d8b640"></div>
<div class="abs badge" style="left:574px;width:74px;background:#d8d8d8"></div>
<div class="abs badge" style="left:671px;width:82px;background:#1f5a96"></div>

</body>
</html>
```